Garlic Farm for Farm Sales/Restaurant sales

Need a professional, but appealing to agriculture world. We are selling 27 kinds of Organic Garlic from a farm in Simla,CO. I have uploaded logo and business information-we are going to need a template, because I will need to use it for four separate people.
-We are trying to appeal to Farm to table restaurants
-As well as growers/farmers

Target Market(s)

Agriculture Sales/Restaurants-Organic

Industry/Entity Type

Agriculture

Contact Information for Business Card

Want it to look more unique then your average orbel mart card- I want it to look amazing

Font styles to use
Sans Serif

Colors
0455a3
ec1f27
fbed22
ffffff

Requirements
Must have
• Just be creative
Nice to have
• Colorful
Should not have
• plain

```html
<!DOCTYPE html>
<html lang="en">
<head>
<meta charset="utf-8">
<title>Summit Ridge Garlic Co. – Business Card</title>
<link href="https://fonts.googleapis.com/css2?family=Open+Sans:wght@400;600&display=swap" rel="stylesheet">
<style>
  :root {
    --brand-blue: #0455a3;
    --brand-red: #ec1f27;
    --brand-yellow: #fbed22;
    --paper: #f1f1f1;
    --ink: #1a1a1a;
    --stage: #d8d8d8;
  }
  * { box-sizing: border-box; margin: 0; padding: 0; }
  html, body { width: 1200px; height: 1200px; overflow: hidden; }
  body {
    background: var(--stage);
    font-family: "Open Sans", sans-serif;
    position: relative;
  }
  .card {
    position: absolute;
    left: 250px;
    width: 700px;
    height: 400px;
    overflow: hidden;
  }
  .card--front { top: 150px; background: var(--paper); }
  .card--back { top: 650px; background: var(--brand-blue); }

  /* logo tiles */
  .logo-tile {
    position: absolute;
    display: flex;
    align-items: center;
    justify-content: center;
    gap: 8px;
  }
  .logo-tile__dot {
    width: 26px; height: 26px;
    border-radius: 50%;
    background: var(--brand-red);
    flex: none;
  }
  .logo-tile__name {
    font-weight: 600;
    font-size: 19px;
    letter-spacing: 0.5px;
    white-space: nowrap;
  }
  .card--front .logo-tile {
    left: 36px; top: 0; width: 148px; height: 186px;
    background: var(--brand-blue);
    flex-direction: column;
  }
  .card--front .logo-tile__name { color: #fff; }
  .card--back .logo-tile {
    left: 258px; top: 0; width: 150px; height: 160px;
    background: var(--paper);
    flex-direction: column;
  }
  .card--back .logo-tile__name { color: var(--brand-blue); }

  .tile-rules { position: absolute; }
  .card--front .tile-rules { left: 30px; top: 186px; }
  .card--back .tile-rules { left: 252px; top: 160px; }

  /* front contact block */
  .contact {
    position: absolute;
    left: 214px;
    top: 44px;
    color: var(--ink);
  }
  .contact__name {
    font-size: 21px;
    font-weight: 400;
    letter-spacing: 1px;
    margin-bottom: 6px;
  }
  .contact__line {
    font-size: 15.5px;
    letter-spacing: 1px;
    line-height: 20px;
  }

  .band { position: absolute; background: var(--brand-blue); }
  .band--short { left: 0; top: 236px; width: 170px; height: 22px; }
  .band--long {
    left: 196px; top: 272px; width: 504px; height: 22px;
    color: #fff;
    font-size: 14.5px;
    letter-spacing: 0.6px;
    line-height: 22px;
    padding-left: 6px;
    white-space: nowrap;
  }

  /* back social row */
  .follow {
    position: absolute;
    left: 300px;
    top: 198px;
    color: #fff;
    font-size: 16px;
    letter-spacing: 2px;
  }
  .social {
    position: absolute;
    left: 232px;
    top: 236px;
    display: flex;
    gap: 12px;
    list-style: none;
  }
  .social__item {
    width: 18px; height: 18px;
    background: #fff;
    border-radius: 2px;
  }
</style>
</head>
<body>

<section class="card card--front" aria-label="Business card front">
  <div class="logo-tile">
    <span class="logo-tile__dot"></span>
    <span class="logo-tile__name">summit ridge</span>
  </div>
  <svg class="tile-rules" width="160" height="30" viewBox="0 0 160 30">
    <line x1="0" y1="4" x2="150" y2="4" stroke="var(--brand-blue)" stroke-width="3"/>
    <line x1="2" y1="13" x2="152" y2="13" stroke="var(--brand-blue)" stroke-width="3"/>
    <line x1="4" y1="22" x2="154" y2="22" stroke="var(--brand-blue)" stroke-width="3"/>
  </svg>

  <div class="contact">
    <p class="contact__name">DANA WHITLOW</p>
    <p class="contact__line">P : 555-014-2290</p>
    <p class="contact__line">M: dana@srgarlic.com</p>
    <p class="contact__line">W: www.srgarlic.com</p>
    <p class="contact__line">A : P.O. Box 48 Pinecrest, CO&nbsp; 80999</p>
  </div>

  <div class="band band--short"></div>
  <div class="band band--long">Summit Ridge Garlic Co., LLC</div>
</section>

<section class="card card--back" aria-label="Business card back">
  <div class="logo-tile">
    <span class="logo-tile__dot"></span>
    <span class="logo-tile__name">summit ridge</span>
  </div>
  <svg class="tile-rules" width="160" height="30" viewBox="0 0 160 30">
    <line x1="0" y1="4" x2="150" y2="4" stroke="var(--paper)" stroke-width="3"/>
    <line x1="2" y1="13" x2="152" y2="13" stroke="var(--paper)" stroke-width="3"/>
    <line x1="4" y1="22" x2="154" y2="22" stroke="var(--paper)" stroke-width="3"/>
  </svg>

  <p class="follow">FOLLOW US</p>
  <ul class="social" aria-label="Social profiles">
    <li class="social__item"></li>
    <li class="social__item"></li>
    <li class="social__item"></li>
    <li class="social__item"></li>
  </ul>
</section>

</body>
</html>
```